Carpentry Fitouts business Van half wrap

We are looking for a half wrap on our 2020Mitsubishi Express van.
Template attached, base colour to be white

Van colour is white. The 2 blue colours from logo plus black should be used in the half wrap

Our services are :
Commercial Carpentry
Interior Fitouts
Plastering
Suspended Ceilings
Windows & Doors

Rear window to have perforated one way film

Contact details on van should be PH:0413 926 058
dale@keelbrookfitouts.com.au

Industry/Entity Type

Carpentry Fitouts

Colors
0054AA
0677BA
7BADD7
CADEEF
E8F1F8
0094D4
00A9DD
6FCCEA
C7EBF8
E9F6FB

Requirements
Nice to have
• Wrap not through door handles

```html
<!DOCTYPE html>
<html lang="en">
<head>
<meta charset="utf-8">
<title>Keelbrook Fitouts – Van Half Wrap</title>
<link rel="stylesheet" href="https://fonts.googleapis.com/css2?family=Antonio:wght@400&family=Archivo:wght@600;700&display=swap">
<style>
  :root{
    --canvas:#eef1f4;
    --van-white:#ffffff;
    --trim:#2e3033;
    --glass:#3a4046;
    --navy:#1f2568;
    --teal:#0094d4;
    --teal-light:#00a9dd;
    --tyre:#1c1d1f;
    --rim:#c9ccd0;
  }
  html,body{margin:0;padding:0;width:1200px;height:599px;overflow:hidden;background:var(--canvas);}
  .wrap-board{display:block;width:1200px;height:599px;}
  .brand-name{font-family:"Antonio",sans-serif;font-weight:400;fill:#fff;}
  .service-list{font-family:"Archivo",sans-serif;font-weight:600;fill:#fff;font-size:14px;letter-spacing:.2px;}
  .contact-phone{font-family:"Archivo",sans-serif;font-weight:700;fill:var(--navy);font-size:29px;}
  .contact-email{font-family:"Archivo",sans-serif;font-weight:600;fill:var(--teal);font-size:16px;}
  .bullet{fill:var(--teal-light);}
</style>
</head>
<body>
<svg class="wrap-board" viewBox="0 0 1730 864" xmlns="http://www.w3.org/2000/svg" role="img" aria-label="Side view of a white van with Keelbrook Fitouts half wrap">
  <defs>
    <linearGradient id="rear-panel-fade" x1="0" y1="0" x2="0" y2="1">
      <stop offset="0" stop-color="var(--teal)"/>
      <stop offset=".35" stop-color="var(--teal)"/>
      <stop offset=".62" stop-color="var(--navy)"/>
      <stop offset="1" stop-color="var(--navy)"/>
    </linearGradient>
    <clipPath id="van-body-clip">
      <path d="M120 520 Q118 450 170 410 L320 340 Q400 250 500 175 Q540 150 620 148 L1520 135 Q1548 136 1555 170 L1578 560 L1590 600 L1585 640 L140 660 Q112 640 112 600 Z"/>
    </clipPath>
  </defs>

  <!-- van body -->
  <g class="van-body">
    <path d="M120 520 Q118 450 170 410 L320 340 Q400 250 500 175 Q540 150 620 148 L1520 135 Q1548 136 1555 170 L1578 560 L1590 600 L1585 640 L140 660 Q112 640 112 600 Z" fill="var(--van-white)"/>
    <g clip-path="url(#van-body-clip)">
      <!-- wrap: navy diagonal sweep and rear gradient panel -->
      <polygon class="wrap-sweep" points="615,670 1100,140 1600,130 1600,670" fill="url(#rear-panel-fade)"/>
      <polygon class="wrap-wedge" points="615,670 760,515 1200,515 1200,670" fill="var(--navy)"/>
      <!-- rear dark pillar -->
      <rect x="1490" y="130" width="110" height="560" fill="var(--trim)"/>
      <!-- lower trim -->
      <path d="M110 500 L110 670 L500 670 L500 600 Q470 520 370 520 Q270 520 250 600 L240 520 Z" fill="var(--trim)"/>
      <rect x="520" y="590" width="660" height="40" fill="var(--trim)" opacity=".85"/>
      <rect x="1400" y="560" width="200" height="110" fill="var(--trim)"/>
    </g>
    <!-- rear lamp -->
    <path d="M1535 260 L1560 260 L1568 400 L1540 405 Z" fill="#b3262b"/>
    <!-- cab window -->
    <path d="M440 350 L470 290 Q560 205 640 190 L770 182 Q780 182 778 195 L770 360 Q768 378 750 378 L450 380 Q432 378 440 350 Z" fill="var(--glass)"/>
    <!-- mirror -->
    <path d="M455 320 Q460 295 490 298 L515 300 L515 362 L470 366 Q452 362 455 340 Z" fill="var(--trim)"/>
    <!-- door seams -->
    <line x1="795" y1="150" x2="795" y2="630" stroke="#999" stroke-width="2" opacity=".5"/>
    <line x1="1190" y1="145" x2="1190" y2="630" stroke="#111" stroke-width="2" opacity=".35"/>
    <!-- door handles (left unwrapped) -->
    <rect x="697" y="420" width="78" height="12" rx="5" fill="var(--trim)"/>
    <rect x="868" y="415" width="82" height="12" rx="5" fill="var(--trim)"/>
    <!-- headlamp -->
    <path d="M140 470 Q160 420 230 395 L300 375 Q250 430 200 465 Z" fill="#c6ccd2"/>
  </g>

  <!-- wheels -->
  <g class="wheel">
    <circle cx="370" cy="640" r="105" fill="var(--tyre)"/>
    <circle cx="370" cy="640" r="65" fill="var(--rim)"/>
    <circle cx="370" cy="640" r="30" fill="#2a2b2d"/>
  </g>
  <g class="wheel">
    <circle cx="1315" cy="630" r="105" fill="var(--tyre)"/>
    <circle cx="1315" cy="630" r="65" fill="var(--rim)"/>
    <circle cx="1315" cy="630" r="30" fill="#2a2b2d"/>
  </g>

  <!-- brand name -->
  <text class="brand-name" x="1118" y="340" font-size="112" textLength="348" lengthAdjust="spacingAndGlyphs">KEELBROOK FITOUTS</text>

  <!-- services -->
  <g class="service-list">
    <circle class="bullet" cx="1121" cy="410" r="4.5"/>
    <text x="1129" y="415">COMMERCIAL CARPENTRY</text>
    <circle class="bullet" cx="1326" cy="410" r="4.5"/>
    <text x="1334" y="415">INTERIOR FITOUTS</text>
    <circle class="bullet" cx="1155" cy="429" r="4.5"/>
    <text x="1164" y="434">PLASTERING</text>
    <circle class="bullet" cx="1262" cy="429" r="4.5"/>
    <text x="1270" y="434">SUSPENDED CEILINGS</text>
    <circle class="bullet" cx="1215" cy="448" r="4.5"/>
    <text x="1223" y="453">WINDOWS &amp; DOORS</text>
  </g>

  <!-- contact -->
  <g class="contact">
    <path d="M463 458 q-4 4 0 10 l4 5 q6 6 12 4 l3 -3 -5 -5 -3 2 q-4 -2 -7 -7 l2 -3 -5 -5 z" fill="var(--teal)"/>
    <path d="M474 456 a9 9 0 0 1 9 9 M474 461 a4 4 0 0 1 4 4" stroke="var(--teal)" stroke-width="2" fill="none"/>
    <text class="contact-phone" x="489" y="474">0413 926 058</text>
    <text class="contact-email" x="460" y="493">dale@keelbrookfitouts.com.au</text>
  </g>
</svg>
</body>
</html>
```